Tech business card design

We need an amazing business card design for our new business 'Brakka' a marketing tech startup based in Sydney, Australia. We provide an online marketplace for businesses to search and buy advertising media, connect with service providers and learn more about marketing. We wish to communicate 'cool tech', reliability and professionalism and design based around our logo.

Target Market(s)

Business Owners

Contact Information for Business Card

Name
Position
Email Address
Website
Phone Number

Font styles to use
Other font styles liked:
• Avenir & Avenir Next

Colors

Designer to choose colors to be used in the design.

```html
<!DOCTYPE html>
<html lang="en">
<head>
<meta charset="utf-8">
<title>Brakka Business Card</title>
<link rel="stylesheet" href="https://fonts.googleapis.com/css2?family=Montserrat:wght@400;500;700;800&display=swap">
<style>
  :root {
    --navy: #1a1b4b;
    --navy-deep: #14153c;
    --paper: #ffffff;
    --paper-shade: #eeeff3;
    --stage: #2b2b2f;
    --ink: #1a1b4b;
  }
  * { margin: 0; padding: 0; box-sizing: border-box; }
  html, body {
    width: 1200px; height: 800px; overflow: hidden;
    background: var(--stage);
    font-family: "Montserrat", sans-serif;
  }
  .stage {
    width: 1200px; height: 800px;
    display: flex; align-items: center; justify-content: center; gap: 40px;
  }
  .card {
    position: relative;
    width: 530px; height: 303px;
    border-radius: 22px;
    overflow: hidden;
  }
  /* Back side */
  .card-back {
    background: linear-gradient(160deg, var(--navy) 0%, var(--navy-deep) 100%);
    color: var(--paper);
    display: flex; flex-direction: column; align-items: center; justify-content: center;
  }
  .card-back .wordmark {
    font-size: 70px; font-weight: 800; letter-spacing: -1px; line-height: 1;
    color: var(--paper);
  }
  .card-back .web {
    margin-top: 34px;
    font-size: 11px; font-weight: 500; letter-spacing: 6px;
    color: var(--paper);
  }
  /* Front side */
  .card-front {
    background: linear-gradient(135deg, var(--paper) 55%, var(--paper-shade) 100%);
    color: var(--ink);
  }
  .rule { position: absolute; left: 0; height: 2px; background: var(--navy); }
  .rule-top { top: 74px; width: 290px; }
  .rule-mid { top: 212px; width: 100%; }
  .base-band {
    position: absolute; left: 0; right: 0; bottom: 0; height: 12px;
    background: var(--navy);
  }
  .name-block {
    position: absolute; top: 46px; left: 290px; width: 214px; height: 58px;
    background: var(--navy); color: var(--paper);
    display: flex; flex-direction: column; align-items: center; justify-content: center;
  }
  .name-block .name { font-size: 22px; font-weight: 700; line-height: 1.1; }
  .name-block .role { font-size: 12px; font-weight: 400; margin-top: 2px; }
  .card-front .wordmark {
    position: absolute; left: 38px; top: 118px;
    font-size: 62px; font-weight: 800; letter-spacing: -1px; line-height: 1;
    color: var(--navy);
  }
  .address {
    position: absolute; right: 26px; top: 126px;
    text-align: right; font-style: normal;
    font-size: 13px; font-weight: 500; line-height: 1.45;
  }
  .contacts {
    position: absolute; left: 38px; top: 226px;
    list-style: none; font-size: 14px; font-weight: 500; line-height: 1.4;
  }
  .contacts li { display: flex; align-items: center; gap: 10px; }
  .contacts svg { width: 13px; height: 13px; flex: none; }
</style>
</head>
<body>
<main class="stage">
  <section class="card card-back" aria-label="Card back">
    <div class="wordmark">brakka</div>
    <div class="web">WWW.BRAKKA.COM</div>
  </section>

  <section class="card card-front" aria-label="Card front">
    <div class="rule rule-top"></div>
    <div class="name-block">
      <div class="name">Liam Carter</div>
      <div class="role">Managing Director</div>
    </div>
    <div class="wordmark">brakka</div>
    <address class="address">
      118 Harbour Street<br>
      Level 6, Sydney<br>
      NSW 2000
    </address>
    <div class="rule rule-mid"></div>
    <ul class="contacts">
      <li>
        <svg viewBox="0 0 16 16" aria-hidden="true"><path fill="#1a1b4b" d="M3.5 1.5l2.5 2.8-1.4 1.8c.9 2 2.5 3.6 4.5 4.5l1.8-1.4 2.8 2.5-1.6 2.3C7.4 13.8 2.2 8.6 1.2 3.1z"/></svg>
        <span>+61 2 8154 7720</span>
      </li>
      <li>
        <svg viewBox="0 0 16 16" aria-hidden="true"><rect x="1" y="3" width="14" height="10" fill="#1a1b4b"/><path d="M1.5 3.5L8 9l6.5-5.5" stroke="#fff" stroke-width="1.3" fill="none"/></svg>
        <span>info@brakka.com</span>
      </li>
      <li>
        <svg viewBox="0 0 16 16" aria-hidden="true"><g fill="none" stroke="#1a1b4b" stroke-width="1.4"><circle cx="8" cy="8" r="6.5"/><ellipse cx="8" cy="8" rx="2.8" ry="6.5"/><path d="M1.5 8h13M2.5 4.8h11M2.5 11.2h11"/></g></svg>
        <span>www.brakka.com</span>
      </li>
    </ul>
    <div class="base-band"></div>
  </section>
</main>
</body>
</html>
```